K.T.L Electrical Services Pty Ltd

Electrical contracting business. I have a base for the design which i like. The contact number needs to be changed to 0491736250 and the O made more solid and level with the rest of the letters. If you have any other ideas of what would make it better I'm happy to see them.

The back side to be written as dot points with the following:
- Residential & Commercial
- Maintenance
- PV & Battery servicing
- EV Chargers

```html
<!DOCTYPE html>
<html lang="en">
<head>
<meta charset="utf-8">
<title>K.T.L Electrical Services Pty Ltd – Business Card</title>
<link href="https://fonts.googleapis.com/css2?family=Montserrat:wght@500;600;700;800&family=Lato:wght@400;700&display=swap" rel="stylesheet">
<style>
  :root {
    --backdrop: #e4e6e6;
    --card: #1f2a2e;
    --teal: #8fb0b0;
    --gold: #f2b81b;
    --white: #ffffff;
    --muted: #d6dede;
  }
  * { box-sizing: border-box; margin: 0; padding: 0; }
  html, body { width: 1200px; height: 800px; overflow: hidden; }
  body {
    background: var(--backdrop);
    display: flex;
    align-items: center;
    justify-content: center;
    gap: 40px;
  }
  .card {
    position: relative;
    width: 540px;
    height: 309px;
    background: var(--card);
    border-radius: 4px;
    box-shadow: 0 10px 30px rgba(0,0,0,0.18);
    overflow: hidden;
    color: var(--white);
  }

  /* Shared business name */
  .business-name {
    display: flex;
    align-items: center;
    font-family: "Montserrat", sans-serif;
    font-weight: 700;
    color: var(--white);
    white-space: nowrap;
  }
  .business-name .name-square {
    background: var(--teal);
    flex: none;
  }

  /* Contact side */
  .card-front .business-name {
    position: absolute;
    right: 30px; top: 30px;
    gap: 8px;
    font-size: 13px;
  }
  .card-front .business-name .name-square { width: 10px; height: 10px; }

  .identity {
    position: absolute;
    left: 30px; top: 82px;
  }
  .identity .person-name {
    font-family: "Montserrat", sans-serif;
    font-weight: 800;
    font-size: 26px;
    letter-spacing: 0.5px;
    color: var(--teal);
    line-height: 1;
  }
  .identity .person-role {
    font-family: "Montserrat", sans-serif;
    font-weight: 600;
    font-size: 15px;
    color: var(--gold);
    margin-top: 6px;
  }
  .card-front .divider {
    position: absolute;
    left: 30px; right: 30px; top: 150px;
    height: 1px;
    background: var(--teal);
  }
  .contact-list {
    position: absolute;
    left: 30px; top: 172px;
    list-style: none;
    font-family: "Lato", sans-serif;
    font-size: 15px;
    color: var(--white);
  }
  .contact-list li {
    display: flex;
    align-items: center;
    gap: 12px;
    height: 30px;
  }
  .contact-list svg { width: 15px; height: 15px; flex: none; }
  .address {
    position: absolute;
    right: 30px; top: 176px;
    text-align: right;
    font-family: "Lato", sans-serif;
    font-style: normal;
    font-size: 13.5px;
    line-height: 1.6;
    color: var(--muted);
  }

  /* Logo and services side */
  .card-back .business-name {
    position: absolute;
    left: 40px; top: 74px;
    gap: 12px;
    font-size: 22px;
  }
  .card-back .business-name .name-square { width: 18px; height: 18px; }

  .card-back .divider {
    position: absolute;
    left: 40px; width: 120px; top: 126px;
    height: 2px;
    background: var(--gold);
  }
  .services {
    position: absolute;
    left: 40px; top: 150px;
    list-style: none;
    font-family: "Montserrat", sans-serif;
    font-weight: 500;
    font-size: 14px;
    letter-spacing: 0.6px;
    text-transform: uppercase;
    color: var(--white);
  }
  .services li {
    display: flex;
    align-items: center;
    gap: 12px;
    height: 26px;
  }
  .services li::before {
    content: "";
    width: 7px; height: 7px;
    border-radius: 50%;
    background: var(--gold);
    flex: none;
  }
</style>
</head>
<body>

  <section class="card card-front" aria-label="Business card, contact side">
    <p class="business-name"><span class="name-square"></span>K.T.L Electrical Services Pty Ltd</p>

    <div class="identity">
      <p class="person-name">DANIEL HARTLEY</p>
      <p class="person-role">Founder &amp; CEO</p>
    </div>

    <div class="divider"></div>

    <ul class="contact-list">
      <li>
        <svg viewBox="0 0 16 16" aria-hidden="true"><path fill="#8fb0b0" d="M3.6 1.5l2.3 2.6-1.3 1.7c.9 2 2.6 3.7 4.6 4.6l1.7-1.3 2.6 2.3-1.2 2.1C7 13.2 2.8 9 2 3.3z"/></svg>
        <span>0491736250</span>
      </li>
      <li>
        <svg viewBox="0 0 16 16" aria-hidden="true"><rect x="1.5" y="3.5" width="13" height="9" rx="1" fill="#8fb0b0"/><path d="M2 4.2l6 4.6 6-4.6" fill="none" stroke="#1f2a2e" stroke-width="1.2"/></svg>
        <span>info@ktlelectricalservices.com</span>
      </li>
      <li>
        <svg viewBox="0 0 16 16" aria-hidden="true"><circle cx="8" cy="8" r="6.5" fill="none" stroke="#8fb0b0" stroke-width="1.4"/><ellipse cx="8" cy="8" rx="2.8" ry="6.5" fill="none" stroke="#8fb0b0" stroke-width="1.2"/><path d="M1.5 8h13" stroke="#8fb0b0" stroke-width="1.2"/></svg>
        <span>ktlelectricalservices.com</span>
      </li>
    </ul>

    <address class="address">
      K.T.L Electrical Services<br>
      423 Street Address Here, City<br>
      State &amp; Country, ZIP Code
    </address>
  </section>

  <section class="card card-back" aria-label="Business card, name and services side">
    <p class="business-name"><span class="name-square"></span>K.T.L Electrical Services Pty Ltd</p>

    <div class="divider"></div>

    <ul class="services">
      <li>Residential &amp; Commercial</li>
      <li>Maintenance</li>
      <li>PV &amp; Battery Servicing</li>
      <li>EV Chargers</li>
    </ul>
  </section>

</body>
</html>
```